Life Coach for Lawyers Business Card Design

Elegant, original, business card design for life coaching service for associate attorneys who work in big law and struggle with stress, overwhelm, and time management. Double sided design.

Target Market(s)

Women associate attorneys who work in big law and struggle with stress, overwhelm, and time management.

Industry/Entity Type

Life Coaching

Contact Information for Business Card

Marissa Pendrell
Life Coach
518.677.3941
calmbriefcounsel.net
marissa@calmbriefcounsel.net
@calmbriefcounsel (Instagram)

Font styles to use
Other font styles liked:
• Silver South font duo. See uploaded files.

Requirements
Must have
• Icons for phone, website, email, and Instagram instead of words. Specific colors used in my logo (171B2B, 421121, FFFFFF)
Nice to have
• Foil. Embossed. Feminine design.
Should not have
• Any colors other than those used in logo. See uploaded files.

```html
<!DOCTYPE html>
<html lang="en">
<head>
<meta charset="utf-8">
<title>Marissa Pendrell – Business Card</title>
<link rel="stylesheet" href="https://fonts.googleapis.com/css2?family=Gilda+Display&family=Montserrat:wght@500&family=Mulish:wght@300&display=swap">
<style>
  :root {
    --page: #ffffff;
    --cream: #f1eedb;
    --ink: #212121;
    --ink-deep: #1a1a1a;
  }
  * { margin: 0; padding: 0; box-sizing: border-box; }
  html, body { width: 1200px; height: 1200px; overflow: hidden; background: var(--page); }
  .canvas { position: relative; width: 1200px; height: 1200px; }

  .card-front {
    position: absolute; left: 283px; top: 106px; width: 611px; height: 350px;
    background: var(--cream);
    display: flex; align-items: center; justify-content: center; gap: 16px;
  }
  .brand-mark {
    width: 22px; height: 22px; border-radius: 50%; background: var(--ink-deep);
  }
  .brand-name {
    font-family: "Montserrat", sans-serif; font-weight: 500;
    font-size: 32px; letter-spacing: 3px; color: var(--ink-deep);
    text-transform: uppercase;
  }

  .card-back {
    position: absolute; left: 414px; top: 537px; width: 349px; height: 610px;
    background: var(--ink);
    color: var(--cream);
  }
  .name {
    position: absolute; top: 48px; left: 0; width: 100%;
    font-family: "Gilda Display", serif; font-weight: 400;
    font-size: 57px; line-height: 58px; text-align: center;
  }
  .title {
    position: absolute; top: 172px; left: 0; width: 100%;
    font-family: "Mulish", sans-serif; font-weight: 300;
    font-size: 24px; letter-spacing: 1.5px; text-align: center;
  }

  .contacts { position: absolute; left: 31px; top: 420px; list-style: none; }
  .contact {
    display: flex; align-items: center; height: 37.5px;
    font-family: "Mulish", sans-serif; font-weight: 300;
    font-size: 15px; letter-spacing: 1.2px;
  }
  .contact svg { width: 17px; height: 17px; margin-right: 14px; flex: none; }
</style>
</head>
<body>
<div class="canvas">
  <section class="card-front">
    <span class="brand-mark"></span>
    <span class="brand-name">Even Keel</span>
  </section>

  <section class="card-back">
    <h1 class="name">Marissa<br>Pendrell</h1>
    <p class="title">Life Coach</p>
    <ul class="contacts">
      <li class="contact">
        <svg viewBox="0 0 20 20" aria-hidden="true">
          <circle cx="10" cy="10" r="8.6" fill="none" stroke="#f1eedb" stroke-width="1.4"/>
          <path d="M7 5.5c.6 0 1.6 1.9 1.5 2.3-.1.5-.9.7-.8 1.2.3 1 1.5 2.3 2.4 2.5.5.1.7-.7 1.2-.8.4-.1 2.2 1 2.2 1.5 0 .6-.9 1.6-1.7 1.6-2.6 0-6.1-3.5-6.1-6.1 0-.8.8-2.2 1.3-2.2z" fill="#f1eedb"/>
        </svg>
        <span>518.677.3941</span>
      </li>
      <li class="contact">
        <svg viewBox="0 0 20 20" aria-hidden="true">
          <circle cx="10" cy="10" r="9.3" fill="#f1eedb"/>
          <path d="M5.5 8l4.5 3 4.5-3v5h-9z M5.5 7l4.5 3 4.5-3z" fill="#212121"/>
        </svg>
        <span>marissa@calmbriefcounsel.net</span>
      </li>
      <li class="contact">
        <svg viewBox="0 0 20 20" aria-hidden="true" fill="none" stroke="#f1eedb" stroke-width="1.3">
          <circle cx="10" cy="10" r="8.6"/>
          <ellipse cx="10" cy="10" rx="3.6" ry="8.6"/>
          <path d="M1.4 10h17.2M2.8 5.5h14.4M2.8 14.5h14.4"/>
        </svg>
        <span>calmbriefcounsel.net</span>
      </li>
      <li class="contact">
        <svg viewBox="0 0 20 20" aria-hidden="true">
          <circle cx="10" cy="10" r="8.6" fill="none" stroke="#f1eedb" stroke-width="1.6"/>
        </svg>
        <span>@calmbriefcounsel</span>
      </li>
    </ul>
  </section>
</div>
</body>
</html>
```